Web Design Project for velbrook

We are looking for a sleek and sophisticated website design for our already developed web-based gallery management software application. Here is a link to our web-app: http://www.vel-brook.co

You will login on the main page and then we would like to include all of the information on the PDF that I am providing below (it outlines what?, where?, why? who? and how much?). Basically, we need a home page, about page, and a pricing page, as well as a sign up page that should be navigable from the upper right hand corner of the site where the sign in/sign up would be located. Also, our 3 tenets are that the software program is "attractive, accessible, and affordable", which might need to be somehow incorporated. There are a few websites that we would like for you to take inspiration from listed below:

https://tidemoxen.com (for homepage)
https://plumwovenly.com (for homepage/pricing page/etc)
https://tidemoxen.com/tour (for a tour of how the product works)

We are currently having a logo designed and will share that as soon as it is available! Also, let us know if you need photos/screen shots, as we can provide them.

Thanks!

Reason: Extending deadline as we are just now getting designs we would like to see fully developed.

Target Market(s)

art galleries, artists, art collectors, art consultants, museums

Industry/Entity Type

Software

Requirements
Must have
• Home page
About page (or tour through the app)
Pricing page
Sign up page (the more click-throughs to signing up the better)

```html
<!DOCTYPE html>
<html lang="en">
<head>
<meta charset="utf-8">
<title>velbrook — Gallery</title>
<link href="https://fonts.googleapis.com/css2?family=Arimo:wght@400;700&display=swap" rel="stylesheet">
<style>
  :root{
    --ink:#555;
    --muted:#a7a7a7;
    --rule:#dcdcdc;
    --frame:#e2e2e2;
    --accent:#5e97b8;
    --link:#72b6d8;
    --active:#7fcdec;
    --panel-head:#f6f6f6;
    --footer:#47bde8;
    --white:#fff;
  }
  *{box-sizing:border-box;margin:0;padding:0}
  html,body{width:1200px;height:900px;overflow:hidden;background:var(--white);
    font-family:"Arimo",Arial,sans-serif;color:var(--ink)}
  .canvas{position:relative;width:1200px;height:900px;overflow:hidden}

  /* gallery grid */
  .gallery-row{position:absolute;left:127px;display:grid;grid-template-columns:repeat(7,115px);column-gap:23.8px}
  .gallery-row--top{top:-105px}
  .gallery-row--main{top:82px}
  .card__frame{width:115px;height:115px;border:1px solid var(--frame);padding:3px;background:var(--white)}
  .card__photo{width:100%;height:100%}
  .card__label{display:flex;align-items:center;gap:8px;height:18px;margin-top:3px;font-size:10px;letter-spacing:.8px;color:#444;padding-left:1px}
  .card__meta{display:flex;justify-content:space-between;align-items:center;border-top:1px solid var(--rule);margin-top:3px;padding:4px 2px 0;font-size:8.5px}
  .card__views{color:var(--link);letter-spacing:.3px}
  .card__buy{display:flex;align-items:center;gap:3px;color:#444;font-size:9px}

  /* pagination */
  .pager{position:absolute;left:127px;top:275px;width:944px;height:48px;border-top:1px solid var(--rule);border-bottom:1px solid var(--rule);
    display:flex;align-items:center;font-size:10px;letter-spacing:.6px;color:#8a8a8a}
  .pager__first{margin-right:16px}
  .pager__pages{display:flex;gap:11px;margin-right:15px}
  .pager__page{width:17px;height:17px;border:1px solid #b9b9b9;border-radius:50%;display:flex;align-items:center;justify-content:center;font-size:8.5px;color:#999;letter-spacing:0}
  .pager__page--active{background:var(--active);border-color:var(--active);color:var(--white);font-weight:700}
  .pager__count{margin-left:auto;margin-right:5px;font-size:10.5px;color:#777}

  /* tops section */
  .tops__title{position:absolute;top:343px;left:0;width:1200px;text-align:center;font-size:19px;font-weight:700;letter-spacing:1px;color:var(--accent)}
  .tops__sub{position:absolute;top:368px;left:0;width:1200px;text-align:center;font-size:11.5px;color:var(--muted)}
  .directory{position:absolute;top:400px;height:255px;border:1px solid #e6e6e6;background:var(--white)}
  .directory__head{height:45px;background:var(--panel-head);display:flex;align-items:center;justify-content:center;gap:10px;font-size:14px;color:var(--accent)}
  .directory__list{list-style:none;text-align:center;padding-top:22px;font-size:12.5px;letter-spacing:.6px;color:var(--muted);line-height:19.6px}
  .directory__more{position:absolute;bottom:0;left:0;right:0;height:22px;border-top:1px solid #e6e6e6;display:flex;align-items:center;justify-content:flex-end;gap:4px;padding-right:8px;font-size:10px;font-style:italic;color:#b0b0b0}
  .directory__more--shaded{background:var(--panel-head)}
  .info-dot{width:11px;height:11px;border-radius:50%;background:#d6d6d6;color:var(--white);font-size:8px;font-style:normal;display:flex;align-items:center;justify-content:center;font-weight:700}

  /* footer */
  .site-footer{position:absolute;left:0;top:682px;width:1200px;height:218px;background:var(--footer);color:var(--white)}
  .brand{position:absolute;left:137px;top:44px;display:flex;align-items:center;gap:9px;font-size:22px;font-weight:700}
  .brand__dot{width:14px;height:14px;border-radius:50%;background:var(--white)}
  .mission{position:absolute;left:140px;top:91px;font-size:12px;font-weight:700;letter-spacing:.4px}
  .mission span{font-weight:400}
  .contact{position:absolute;left:651px;top:91px;display:flex;align-items:center;gap:10px;font-size:12px;font-weight:700;letter-spacing:1.2px}
  .social{position:absolute;left:965px;top:87px;display:flex;gap:21px}
  .social__dot{width:20px;height:20px;border-radius:50%;background:rgba(255,255,255,.85)}
  .footer-nav{position:absolute;left:138px;top:137px;display:flex;align-items:center;font-size:12.5px;letter-spacing:.4px}
  .footer-nav strong{letter-spacing:1px;margin-right:19px}
  .footer-nav a{color:var(--white);text-decoration:none;margin-right:18px}
  .footer-nav a:nth-of-type(4){margin-right:25px}
  .footer-nav a:nth-of-type(5){margin-right:25px}
  .copyright{position:absolute;right:136px;top:138px;font-size:12px;font-weight:700;letter-spacing:1px}
</style>
</head>
<body>
<div class="canvas">

  <!-- partial top row -->
  <section class="gallery-row gallery-row--top">
    <article class="card"><div class="card__frame"><div class="card__photo" role="img" aria-label="Artwork thumbnail" style="background:linear-gradient(#c9c6b8,#6f6a5c)"></div></div>
      <div class="card__label"><svg width="11" height="9" viewBox="0 0 11 9"><path d="M0 0h6l5 4.5L6 9H0z" fill="#9a9a9a"/><circle cx="2.5" cy="2.5" r="1" fill="#fff"/></svg>Name here</div>
      <div class="card__meta"><span class="card__views">Wiewed: 25522</span><span class="card__buy">Buy<svg width="9" height="9" viewBox="0 0 9 9"><path d="M3.5 0h2v3.5H7L4.5 6 2 3.5h1.5zM0 6h1.2v1.8h6.6V6H9v3H0z" fill="#777"/></svg></span></div></article>
    <article class="card"><div class="card__frame"><div class="card__photo" role="img" aria-label="Artwork thumbnail" style="background:linear-gradient(#7a4a2a,#3d2316)"></div></div>
      <div class="card__label"><svg width="11" height="9" viewBox="0 0 11 9"><path d="M0 0h6l5 4.5L6 9H0z" fill="#9a9a9a"/><circle cx="2.5" cy="2.5" r="1" fill="#fff"/></svg>Name here</div>
      <div class="card__meta"><span class="card__views">Wiewed: 25522</span><span class="card__buy">Buy<svg width="9" height="9" viewBox="0 0 9 9"><path d="M3.5 0h2v3.5H7L4.5 6 2 3.5h1.5zM0 6h1.2v1.8h6.6V6H9v3H0z" fill="#777"/></svg></span></div></article>
    <article class="card"><div class="card__frame"><div class="card__photo" role="img" aria-label="Artwork thumbnail" style="background:linear-gradient(#eeeae0,#9a9686)"></div></div>
      <div class="card__label"><svg width="11" height="9" viewBox="0 0 11 9"><path d="M0 0h6l5 4.5L6 9H0z" fill="#9a9a9a"/><circle cx="2.5" cy="2.5" r="1" fill="#fff"/></svg>Name here</div>
      <div class="card__meta"><span class="card__views">Wiewed: 25522</span><span class="card__buy">Buy<svg width="9" height="9" viewBox="0 0 9 9"><path d="M3.5 0h2v3.5H7L4.5 6 2 3.5h1.5zM0 6h1.2v1.8h6.6V6H9v3H0z" fill="#777"/></svg></span></div></article>
    <article class="card"><div class="card__frame"><div class="card__photo" role="img" aria-label="Artwork thumbnail" style="background:linear-gradient(#b9bcc8,#4a4c63)"></div></div>
      <div class="card__label"><svg width="11" height="9" viewBox="0 0 11 9"><path d="M0 0h6l5 4.5L6 9H0z" fill="#9a9a9a"/><circle cx="2.5" cy="2.5" r="1" fill="#fff"/></svg>Name here</div>
      <div class="card__meta"><span class="card__views">Wiewed: 25522</span><span class="card__buy">Buy<svg width="9" height="9" viewBox="0 0 9 9"><path d="M3.5 0h2v3.5H7L4.5 6 2 3.5h1.5zM0 6h1.2v1.8h6.6V6H9v3H0z" fill="#777"/></svg></span></div></article>
    <article class="card"><div class="card__frame"><div class="card__photo" role="img" aria-label="Black and white photograph thumbnail" style="background:linear-gradient(#8a8a8a,#2e2e2e)"></div></div>
      <div class="card__label"><svg width="11" height="9" viewBox="0 0 11 9"><path d="M0 0h6l5 4.5L6 9H0z" fill="#9a9a9a"/><circle cx="2.5" cy="2.5" r="1" fill="#fff"/></svg>Name here</div>
      <div class="card__meta"><span class="card__views">Wiewed: 25522</span><span class="card__buy">Buy<svg width="9" height="9" viewBox="0 0 9 9"><path d="M3.5 0h2v3.5H7L4.5 6 2 3.5h1.5zM0 6h1.2v1.8h6.6V6H9v3H0z" fill="#777"/></svg></span></div></article>
    <article class="card"><div class="card__frame"><div class="card__photo" role="img" aria-label="Photograph thumbnail" style="background:linear-gradient(#6b5a50,#2a2220)"></div></div>
      <div class="card__label"><svg width="11" height="9" viewBox="0 0 11 9"><path d="M0 0h6l5 4.5L6 9H0z" fill="#9a9a9a"/><circle cx="2.5" cy="2.5" r="1" fill="#fff"/></svg>Name here</div>
      <div class="card__meta"><span class="card__views">Wiewed: 25522</span><span class="card__buy">Buy<svg width="9" height="9" viewBox="0 0 9 9"><path d="M3.5 0h2v3.5H7L4.5 6 2 3.5h1.5zM0 6h1.2v1.8h6.6V6H9v3H0z" fill="#777"/></svg></span></div></article>
    <article class="card"><div class="card__frame"><div class="card__photo" role="img" aria-label="Photograph thumbnail" style="background:linear-gradient(#f2ece2,#d8c6a4)"></div></div>
      <div class="card__label"><svg width="11" height="9" viewBox="0 0 11 9"><path d="M0 0h6l5 4.5L6 9H0z" fill="#9a9a9a"/><circle cx="2.5" cy="2.5" r="1" fill="#fff"/></svg>Name here</div>
      <div class="card__meta"><span class="card__views">Wiewed: 25522</span><span class="card__buy">Buy<svg width="9" height="9" viewBox="0 0 9 9"><path d="M3.5 0h2v3.5H7L4.5 6 2 3.5h1.5zM0 6h1.2v1.8h6.6V6H9v3H0z" fill="#777"/></svg></span></div></article>
  </section>

  <!-- main row -->
  <section class="gallery-row gallery-row--main">
    <article class="card"><div class="card__frame"><div class="card__photo" role="img" aria-label="Painted portrait artwork in red and ochre" style="background:linear-gradient(135deg,#c9b46a,#a6402c 60%,#5a3a22)"></div></div>
      <div class="card__label"><svg width="11" height="9" viewBox="0 0 11 9"><path d="M0 0h6l5 4.5L6 9H0z" fill="#9a9a9a"/><circle cx="2.5" cy="2.5" r="1" fill="#fff"/></svg>Name here</div>
      <div class="card__meta"><span class="card__views">Wiewed: 25522</span><span class="card__buy">Buy<svg width="9" height="9" viewBox="0 0 9 9"><path d="M3.5 0h2v3.5H7L4.5 6 2 3.5h1.5zM0 6h1.2v1.8h6.6V6H9v3H0z" fill="#777"/></svg></span></div></article>
    <article class="card"><div class="card__frame"><div class="card__photo" role="img" aria-label="Gold floral illustration on brown" style="background:radial-gradient(circle at 50% 60%,#a0692d,#6e3f1c)"></div></div>
      <div class="card__label"><svg width="11" height="9" viewBox="0 0 11 9"><path d="M0 0h6l5 4.5L6 9H0z" fill="#9a9a9a"/><circle cx="2.5" cy="2.5" r="1" fill="#fff"/></svg>Name here</div>
      <div class="card__meta"><span class="card__views">Wiewed: 25522</span><span class="card__buy">Buy<svg width="9" height="9" viewBox="0 0 9 9"><path d="M3.5 0h2v3.5H7L4.5 6 2 3.5h1.5zM0 6h1.2v1.8h6.6V6H9v3H0z" fill="#777"/></svg></span></div></article>
    <article class="card"><div class="card__frame"><div class="card__photo" role="img" aria-label="Close-up portrait photograph in warm shadow" style="background:linear-gradient(90deg,#2a1a14,#7a5240 55%,#b08066)"></div></div>
      <div class="card__label"><svg width="11" height="9" viewBox="0 0 11 9"><path d="M0 0h6l5 4.5L6 9H0z" fill="#9a9a9a"/><circle cx="2.5" cy="2.5" r="1" fill="#fff"/></svg>Name here</div>
      <div class="card__meta"><span class="card__views">Wiewed: 25522</span><span class="card__buy">Buy<svg width="9" height="9" viewBox="0 0 9 9"><path d="M3.5 0h2v3.5H7L4.5 6 2 3.5h1.5zM0 6h1.2v1.8h6.6V6H9v3H0z" fill="#777"/></svg></span></div></article>
    <article class="card"><div class="card__frame"><div class="card__photo" role="img" aria-label="Night photograph of dewy grass" style="background:radial-gradient(circle at 60% 50%,#2f6a4c,#0c1a22)"></div></div>
      <div class="card__label"><svg width="11" height="9" viewBox="0 0 11 9"><path d="M0 0h6l5 4.5L6 9H0z" fill="#9a9a9a"/><circle cx="2.5" cy="2.5" r="1" fill="#fff"/></svg>Name here</div>
      <div class="card__meta"><span class="card__views">Wiewed: 25522</span><span class="card__buy">Buy<svg width="9" height="9" viewBox="0 0 9 9"><path d="M3.5 0h2v3.5H7L4.5 6 2 3.5h1.5zM0 6h1.2v1.8h6.6V6H9v3H0z" fill="#777"/></svg></span></div></article>
    <article class="card"><div class="card__frame"><div class="card__photo" role="img" aria-label="Black and white photograph on a forest path" style="background:linear-gradient(#4a4a4a,#9a9a9a 70%,#c8c8c8)"></div></div>
      <div class="card__label"><svg width="11" height="9" viewBox="0 0 11 9"><path d="M0 0h6l5 4.5L6 9H0z" fill="#9a9a9a"/><circle cx="2.5" cy="2.5" r="1" fill="#fff"/></svg>Name here</div>
      <div class="card__meta"><span class="card__views">Wiewed: 25522</span><span class="card__buy">Buy<svg width="9" height="9" viewBox="0 0 9 9"><path d="M3.5 0h2v3.5H7L4.5 6 2 3.5h1.5zM0 6h1.2v1.8h6.6V6H9v3H0z" fill="#777"/></svg></span></div></article>
    <article class="card"><div class="card__frame"><div class="card__photo" role="img" aria-label="Black and white street photograph" style="background:linear-gradient(90deg,#d0d0d0,#7a7a7a 50%,#2a2a2a)"></div></div>
      <div class="card__label"><svg width="11" height="9" viewBox="0 0 11 9"><path d="M0 0h6l5 4.5L6 9H0z" fill="#9a9a9a"/><circle cx="2.5" cy="2.5" r="1" fill="#fff"/></svg>Name here</div>
      <div class="card__meta"><span class="card__views">Wiewed: 25522</span><span class="card__buy">Buy<svg width="9" height="9" viewBox="0 0 9 9"><path d="M3.5 0h2v3.5H7L4.5 6 2 3.5h1.5zM0 6h1.2v1.8h6.6V6H9v3H0z" fill="#777"/></svg></span></div></article>
    <article class="card"><div class="card__frame"><div class="card__photo" role="img" aria-label="Monochrome photograph of a canvas sneaker" style="background:radial-gradient(circle at 60% 40%,#b8b4a8,#2c2c2a 75%)"></div></div>
      <div class="card__label"><svg width="11" height="9" viewBox="0 0 11 9"><path d="M0 0h6l5 4.5L6 9H0z" fill="#9a9a9a"/><circle cx="2.5" cy="2.5" r="1" fill="#fff"/></svg>Name here</div>
      <div class="card__meta"><span class="card__views">Wiewed: 25522</span><span class="card__buy">Buy<svg width="9" height="9" viewBox="0 0 9 9"><path d="M3.5 0h2v3.5H7L4.5 6 2 3.5h1.5zM0 6h1.2v1.8h6.6V6H9v3H0z" fill="#777"/></svg></span></div></article>
  </section>

  <!-- pagination -->
  <nav class="pager">
    <span class="pager__first">First page</span>
    <div class="pager__pages">
      <span class="pager__page">1</span><span class="pager__page">2</span><span class="pager__page">3</span>
      <span class="pager__page pager__page--active">4</span><span class="pager__page">5</span><span class="pager__page">6</span>
      <span class="pager__page">7</span><span class="pager__page">8</span><span class="pager__page">9</span>
    </div>
    <span class="pager__next">Next page &gt;</span>
    <span class="pager__count">Showing 1 to 10 of 533 entiers</span>
  </nav>

  <!-- tops -->
  <h2 class="tops__title">The tops on VELBROOK</h2>
  <p class="tops__sub">Art galleries,&nbsp; Artists, Art collectors, Art consultants, Museums</p>

  <section class="directory" style="left:119px;width:160px">
    <header class="directory__head"><svg width="21" height="17" viewBox="0 0 21 17"><rect x="1" y="1" width="19" height="15" fill="none" stroke="#888" stroke-width="2"/><path d="M3 14l5-6 4 4 3-3 4 5z" fill="#888"/><circle cx="14" cy="5" r="1.6" fill="#888"/></svg>Art galleries</header>
    <ul class="directory__list"><li>Art gallery's name</li><li>Art gallery's name</li><li>Art gallery's name</li><li>Art gallery's name</li><li>Art gallery's name</li><li>Art gallery's name</li><li>Art gallery's name</li><li>Art gallery's name</li></ul>
    <div class="directory__more">More <i class="info-dot">i</i></div>
  </section>
  <section class="directory" style="left:295px;width:160px">
    <header class="directory__head"><svg width="21" height="24" viewBox="0 0 21 24"><rect x="1" y="1" width="19" height="14" fill="none" stroke="#888" stroke-width="2"/><rect x="4" y="4" width="6" height="5" fill="#888"/><path d="M12 6h5M12 9h5M4 12h13" stroke="#888" stroke-width="1.5"/><path d="M10.5 15v8M10.5 15l-6 8M10.5 15l6 8" stroke="#888" stroke-width="2"/></svg>Artists</header>
    <ul class="directory__list"><li>Arttis's name</li><li>Arttis's name</li><li>Arttis's name</li><li>Arttis's name</li><li>Arttis's name</li><li>Arttis's name</li><li>Arttis's name</li><li>Arttis's name</li></ul>
    <div class="directory__more">More <i class="info-dot">i</i></div>
  </section>
  <section class="directory" style="left:471px;width:189px">
    <header class="directory__head"><svg width="22" height="19" viewBox="0 0 22 19"><path d="M2 4l12-3 1 3" fill="none" stroke="#888" stroke-width="2"/><rect x="1" y="4" width="19" height="14" rx="1.5" fill="#888"/><rect x="13" y="8.5" width="8" height="5" rx="1" fill="#fff" stroke="#888" stroke-width="1.5"/></svg>Art collectors</header>
    <ul class="directory__list"><li>Art Collecter's name</li><li>Art Collecter's name</li><li>Art Collecter's name</li><li>Art Collecter's name</li><li>Art Collecter's name</li><li>Art Collecter's name</li><li>Art Collecter's name</li><li>Art Collecter's name</li></ul>
    <div class="directory__more directory__more--shaded">More <i class="info-dot">i</i></div>
  </section>
  <section class="directory" style="left:677px;width:189px">
    <header class="directory__head"><svg width="27" height="12" viewBox="0 0 27 12"><rect x="1.5" y="3" width="10" height="7.5" rx="3" fill="none" stroke="#888" stroke-width="2"/><rect x="15.5" y="3" width="10" height="7.5" rx="3" fill="none" stroke="#888" stroke-width="2"/><path d="M11.5 5.5h4M1.5 4L4 1M25.5 4L23 1" stroke="#888" stroke-width="2"/></svg>Art consultants</header>
    <ul class="directory__list"><li>Art Consulant's name</li><li>Art Consulant's name</li><li>Art Consulant's name</li><li>Art Consulant's name</li><li>Art Consulant's name</li><li>Art Consulant's name</li><li>Art Consulant's name</li><li>Art Consulant's name</li></ul>
    <div class="directory__more">More <i class="info-dot">i</i></div>
  </section>
  <section class="directory" style="left:883px;width:189px">
    <header class="directory__head"><svg width="21" height="20" viewBox="0 0 21 20"><path d="M10.5 0L21 5H0z" fill="#888"/><rect x="1" y="6" width="19" height="1.5" fill="#888"/><path d="M3 8.5v8M7.5 8.5v8M13.5 8.5v8M18 8.5v8" stroke="#888" stroke-width="2.2"/><rect x="0" y="17.5" width="21" height="2.5" fill="#888"/></svg>Museums</header>
    <ul class="directory__list"><li>Mesums's name</li><li>Mesums's name</li><li>Mesums's name</li><li>Mesums's name</li><li>Mesums's name</li><li>Mesums's name</li><li>Mesums's name</li><li>Mesums's name</li></ul>
    <div class="directory__more">More <i class="info-dot">i</i></div>
  </section>

  <!-- footer -->
  <footer class="site-footer">
    <div class="brand"><span class="brand__dot"></span>velbrook</div>
    <p class="mission">Our mission is the allery management made easy ! <span>(for example)</span></p>
    <div class="contact"><svg width="21" height="16" viewBox="0 0 21 16"><rect width="21" height="16" fill="rgba(255,255,255,.75)"/><path d="M0 0l10.5 9L21 0M0 16l8-8M21 16l-8-8" fill="none" stroke="#47bde8" stroke-width="1.3"/></svg>CONTACT US</div>
    <div class="social"><span class="social__dot"></span><span class="social__dot"></span><span class="social__dot"></span></div>
    <nav class="footer-nav">
      <strong>Company</strong>
      <a href="#">Home</a><a href="#">Features</a><a href="#">How it Works</a><a href="#">Pricing</a><a href="#">Help &amp; Support</a><a href="#">Community &amp; Feedback</a>
    </nav>
    <div class="copyright">© 2013 velbrook</div>
  </footer>
</div>
</body>
</html>
```